Spring Pet Banner for Veterinary Hospital 5m x 1.2m

Meadowbrook Pet Hospital is a Veterinary Hospital that treats Dogs and Cats. I want a new poster to go on our front fence for spring. It's 5m x 1.2m. I want a design that is eye catching from a nearby road that promotes preventative health measures to get ready for spring.
I have attached images that we commonly use in our branding. I would like images that suite the mood of these images.
EDIT: I have just uploaded a design that I knocked up. I think it sends a clear message.....but I am not a graphic designer or marketing expert, so you can make a similar design if you want and clean it up.

The plan I had for the design is not working. I have simplified the plan so designers can use their own ideas.

Target Market(s)

Women Aged 18 to 60.

Industry/Entity Type

Veterinary

Font styles to use
Sans Serif

Colors
9bcb3b
f78f20
f37122

Requirements
Must have
• Visible from road 30m away.
• Spring.
• A call to action.
• Compliment existing branding.
Nice to have
• Gives people a reason to bring their animals to us now.
Should not have
• Clip art.

```html
<!DOCTYPE html>
<html lang="en">
<head>
<meta charset="utf-8">
<title>Spring Is Perfect For Pets – Meadowbrook Pet Hospital</title>
<link rel="stylesheet" href="https://fonts.googleapis.com/css2?family=Poppins:ital,wght@0,400;0,500;0,800;1,800&family=Kaushan+Script&display=swap">
<style>
  :root {
    --stage: #e6e6e8;
    --paper: #ffffff;
    --orange: #f39a2c;
    --orange-deep: #f37122;
    --peach: #ef8f55;
    --brown: #b5734f;
    --ink: #2d2118;
    --text: #2e2e2e;
    --yellow: #f4f21e;
    --leaf: #9bcb3b;
    --stop: #e0141b;
  }
  * { margin: 0; padding: 0; box-sizing: border-box; }
  html, body {
    width: 1200px; height: 466px; overflow: hidden;
    background: var(--stage);
  }
  .banner {
    position: absolute; left: 20px; top: 76px;
    width: 1160px; height: 314px;
    box-shadow: 0 2px 8px rgba(0,0,0,.18);
  }
  .banner svg { display: block; width: 100%; height: 100%; }
  .tab-text { font-family: "Poppins", sans-serif; font-weight: 800; font-style: italic; fill: var(--paper); font-size: 23px; paint-order: stroke; stroke: var(--ink); stroke-width: 3px; }
  .threat-label { font-family: "Poppins", sans-serif; font-weight: 400; font-size: 12.5px; fill: var(--text); text-anchor: middle; }
  .headline-script { font-family: "Kaushan Script", cursive; font-size: 92px; fill: var(--paper); paint-order: stroke; stroke: var(--ink); stroke-width: 11px; stroke-linejoin: round; }
  .headline-sub { font-family: "Poppins", sans-serif; font-weight: 800; font-style: italic; paint-order: stroke; stroke: var(--ink); stroke-width: 5px; stroke-linejoin: round; }
  .headline-sub .accent { fill: var(--yellow); }
  .headline-sub .plain { fill: var(--paper); }
  .clinic-name { font-family: "Poppins", sans-serif; font-weight: 500; fill: #5a3a26; text-anchor: middle; }
  .cta-text { font-family: "Poppins", sans-serif; font-weight: 800; font-style: italic; font-size: 29px; fill: var(--paper); paint-order: stroke; stroke: var(--ink); stroke-width: 5px; text-anchor: middle; }
</style>
</head>
<body>
<div class="banner">
<svg viewBox="0 0 1232 333" xmlns="http://www.w3.org/2000/svg">
  <defs>
    <linearGradient id="photo-tones" x1="0" y1="0" x2="1" y2="1">
      <stop offset="0" stop-color="#5f8a3c"/>
      <stop offset=".45" stop-color="#d9b06a"/>
      <stop offset="1" stop-color="#c99752"/>
    </linearGradient>
    <linearGradient id="cta-fill" x1="0" y1="0" x2="0" y2="1">
      <stop offset="0" stop-color="#f7b048"/>
      <stop offset="1" stop-color="#ea7f16"/>
    </linearGradient>
    <radialGradient id="cell-tone"><stop offset="0" stop-color="#e3b3e0"/><stop offset="1" stop-color="#a45aa8"/></radialGradient>
    <radialGradient id="flea-tone"><stop offset="0" stop-color="#f4efe8"/><stop offset="1" stop-color="#d8cfc5"/></radialGradient>
    <radialGradient id="worm-tone"><stop offset="0" stop-color="#f2c27a"/><stop offset="1" stop-color="#c8641e"/></radialGradient>
    <radialGradient id="tick-tone"><stop offset="0" stop-color="#ffffff"/><stop offset="1" stop-color="#e8e4e0"/></radialGradient>
    <radialGradient id="heart-tone"><stop offset="0" stop-color="#c8433b"/><stop offset="1" stop-color="#7d1612"/></radialGradient>
  </defs>

  <!-- base -->
  <rect class="paper" width="1232" height="333" fill="var(--paper)"/>

  <!-- top accent stripe -->
  <path d="M420 0 H1232 V6 H520 C480 6 450 10 420 20 Z" fill="var(--orange)"/>

  <!-- hero photo -->
  <path d="M300 0 C380 40 395 230 330 333" fill="none" stroke="var(--brown)" stroke-width="6"/>
  <path role="img" aria-label="Photo: smiling girl hugging a golden retriever in a spring park"
        d="M0 0 H298 C372 42 386 226 322 333 H0 Z" fill="url(#photo-tones)"/>

  <!-- bottom wave -->
  <path d="M0 300 C330 322 690 300 1000 238 C1080 224 1160 218 1232 214 V333 H0 Z" fill="var(--peach)"/>
  <path d="M0 292 C330 314 690 292 1000 230 C1080 216 1160 210 1232 206" fill="none" stroke="var(--brown)" stroke-width="3"/>
  <path d="M920 333 C960 300 990 262 1040 246 C1110 232 1170 230 1232 230 V333 Z" fill="var(--paper)"/>
  <path d="M140 333 C420 318 700 300 930 262" fill="none" stroke="var(--paper)" stroke-width="3"/>

  <!-- section tabs -->
  <g class="tab">
    <path d="M556 6 H786 V44 H562 Q556 44 556 38 Z" fill="var(--brown)"/>
    <text class="tab-text" x="671" y="33" text-anchor="middle">And Parasites</text>
  </g>
  <g class="tab">
    <path d="M957 6 H1232 V44 H968 Q957 44 957 34 Z" fill="var(--orange)"/>
    <text class="tab-text" x="1090" y="33" text-anchor="middle">Protect The Pets</text>
  </g>

  <!-- parasite threats -->
  <g class="threat">
    <circle role="img" aria-label="Microscope image of parvovirus-infected cells" cx="462" cy="143" r="49" fill="url(#cell-tone)"/>
    <circle cx="462" cy="143" r="45" fill="none" stroke="var(--stop)" stroke-width="5"/>
    <line x1="430" y1="111" x2="494" y2="175" stroke="var(--stop)" stroke-width="5"/>
    <line x1="462" y1="197" x2="462" y2="206" stroke="#999" stroke-dasharray="2 2"/>
    <text class="threat-label" x="462" y="225">PARVO</text>
  </g>
  <g class="threat">
    <circle role="img" aria-label="Close-up photo of a flea" cx="564" cy="143" r="49" fill="url(#flea-tone)"/>
    <circle cx="564" cy="143" r="45" fill="none" stroke="var(--stop)" stroke-width="5"/>
    <line x1="532" y1="111" x2="596" y2="175" stroke="var(--stop)" stroke-width="5"/>
    <line x1="564" y1="197" x2="564" y2="206" stroke="#999" stroke-dasharray="2 2"/>
    <text class="threat-label" x="564" y="225">FLEAS</text>
  </g>
  <g class="threat">
    <circle role="img" aria-label="Photo of intestinal worms" cx="667" cy="143" r="49" fill="url(#worm-tone)"/>
    <circle cx="667" cy="143" r="45" fill="none" stroke="var(--stop)" stroke-width="5"/>
    <line x1="635" y1="111" x2="699" y2="175" stroke="var(--stop)" stroke-width="5"/>
    <line x1="667" y1="197" x2="667" y2="206" stroke="#999" stroke-dasharray="2 2"/>
    <text class="threat-label" x="667" y="225">INTESTINAL</text>
    <text class="threat-label" x="667" y="242">WORMS</text>
  </g>
  <g class="threat">
    <circle role="img" aria-label="Close-up photo of a tick" cx="777" cy="143" r="49" fill="url(#tick-tone)"/>
    <circle cx="777" cy="143" r="45" fill="none" stroke="var(--stop)" stroke-width="5"/>
    <line x1="745" y1="111" x2="809" y2="175" stroke="var(--stop)" stroke-width="5"/>
    <line x1="777" y1="197" x2="777" y2="206" stroke="#999" stroke-dasharray="2 2"/>
    <text class="threat-label" x="777" y="225">TICKS</text>
  </g>
  <g class="threat">
    <circle role="img" aria-label="Photo of heartworms in a heart" cx="882" cy="143" r="49" fill="url(#heart-tone)"/>
    <circle cx="882" cy="143" r="45" fill="none" stroke="var(--stop)" stroke-width="5"/>
    <line x1="850" y1="111" x2="914" y2="175" stroke="var(--stop)" stroke-width="5"/>
    <line x1="882" y1="197" x2="882" y2="206" stroke="#999" stroke-dasharray="2 2"/>
    <text class="threat-label" x="882" y="225">HEARTWORM</text>
  </g>

  <!-- clinic name -->
  <g class="clinic">
    <circle cx="1095" cy="116" r="22" fill="var(--leaf)"/>
    <text class="clinic-name" x="1095" y="175" font-size="21">Meadowbrook</text>
    <text class="clinic-name" x="1095" y="199" font-size="21">Pet Hospital</text>
  </g>

  <!-- headline -->
  <text class="headline-script" x="14" y="282">Spring</text>
  <text class="headline-sub" x="102" y="311" font-size="23"><tspan class="accent">Is Perfect</tspan></text>
  <text class="headline-sub" x="248" y="309" font-size="25"><tspan class="plain">For </tspan><tspan class="accent" font-size="38">Pets</tspan></text>

  <!-- call to action -->
  <g class="cta">
    <rect x="952" y="254" width="238" height="56" rx="10" fill="url(#cta-fill)" stroke="#d06a12" stroke-width="2"/>
    <text class="cta-text" x="1071" y="293">Book Online</text>
    <path d="M1192 300 l8 8 l4 -4 l6 6 l6 -2 l-4 10 h-12 l-10 -10 z" fill="var(--paper)" stroke="var(--ink)" stroke-width="2" stroke-linejoin="round"/>
  </g>
</svg>
</div>
</body>
</html>
```